Summer Sale Graphics for Social Media

I want to create 11 social media graphics (new Instagram size 4:5 (1080 x 1350 pixels) focusing on our Summer Sale Graphics, using any of the pics attached. Use the attached pics, NO RANDOM STOCK PHOTOGRAPHY. For the color scheme of the graphics, they should all be complementary to the product colors in the photos.
You can add any of the photos attached but none are required. You can do some of the graphics in all text. I mainly need BOLD text that says one of the headlines (11 total) SEE ATTACHED WORD DOCUMENT for the headlines to use.

```html
<!DOCTYPE html>
<html lang="en">
<head>
<meta charset="utf-8">
<title>Summer Sale Social Graphics</title>
<link rel="stylesheet" href="https://fonts.googleapis.com/css2?family=Bebas+Neue&display=swap">
<style>
:root{
  --board:#8c8c8c;
  --plum:#8a4f86;
  --plum-deep:#6e3a72;
  --navy:#2c3773;
  --navy-deep:#1f2a5e;
  --royal:#1c4f93;
  --magenta:#b33b8c;
  --red:#e8262a;
  --forest:#2d5a45;
  --gold:#f5b51b;
  --tag-blue:#3a5bc7;
  --white:#ffffff;
  --ink:#222222;
}
*{margin:0;padding:0;box-sizing:border-box}
html,body{width:1200px;height:748px;overflow:hidden;background:var(--board)}
body{position:relative;font-family:"Bebas Neue",Impact,sans-serif;color:var(--white);line-height:.9}
.tile{position:absolute;overflow:hidden}
.tile *{position:absolute}
.photo{inset:0}
.hero{left:39px;top:34px;width:545px;height:681px;background:linear-gradient(90deg,var(--plum) 0%,#94608f 45%,#a87a86 70%,#9a6d70 100%)}
.hero .photo{left:230px;background:linear-gradient(180deg,#b48a7c 0%,#c9b3bb 40%,#e9e3ea 60%,#3a2c35 85%,#d9d0d3 100%);opacity:.55}
.hero .headline{left:33px;top:38px;font-size:72px;line-height:62px}
.hero .sale-box{left:34px;top:302px;width:202px;height:240px;border:2px solid var(--white)}
.hero .sale-box span{left:12px;font-size:124px;line-height:1}
.hero .tag{left:34px;top:596px;height:34px;padding:0 8px;background:var(--white);color:var(--plum);font-size:29px;line-height:36px}
.t-col1{left:605px}.t-col2{left:792px}.t-col3{left:978px}
.t-row1{top:35px}.t-row2{top:265px}.t-row3{top:496px}
.small{width:175px;height:218px}
.white{background:var(--white)}
.center{left:0;right:0;text-align:center}
.products{left:10px;right:10px;top:106px;height:88px;background:linear-gradient(180deg,#f4f4f4 0%,#ecebee 50%,#e1dbe3 100%);border-radius:4px}
.tag-s{height:11px;padding:0 4px;font-size:9px;line-height:12px}
.red-box{background:var(--red);color:var(--white)}
.t1 .kicker{top:15px;font-size:16px;color:var(--magenta)}
.t1 .big{top:28px;font-size:42px;color:var(--magenta)}
.t1 .red-box{left:28px;top:63px;width:120px;height:28px;font-size:33px;line-height:30px;text-align:center}
.t1 .tag-s,.t3 .tag-s{left:61px;top:201px;background:var(--forest)}
.t2{background:var(--plum)}
.t2 .photo{background:linear-gradient(90deg,#8a4f86 0%,#a27b8a 40%,#c6b6b8 70%,#6a4a44 100%)}
.t2 .lines{left:6px;top:10px;font-size:17px;line-height:14px}
.t2 .vertical{left:-55px;top:110px;width:155px;font-size:49px;color:var(--gold);transform:rotate(-90deg);white-space:nowrap}
.t2 .tag-box{left:138px;top:195px;width:31px;height:23px;background:#1c1c22;font-size:9px;line-height:10px;text-align:center;padding-top:2px}
.t3 .lines{top:15px;font-size:19px;line-height:17px;color:var(--forest)}
.t3 .red-box{left:27px;top:68px;width:120px;height:28px;font-size:33px;line-height:30px;text-align:center}
.t4{background:var(--navy)}
.t4 .photo{left:80px;background:linear-gradient(90deg,var(--navy) 0%,#6b5570 40%,#a27a62 70%,#c8c4c0 100%)}
.t4 .lines{left:8px;top:19px;font-size:21px;line-height:19px}
.t4 .biggest{left:8px;top:80px;font-size:46px;line-height:31px;color:var(--gold)}
.t4 .year{left:8px;top:146px;font-size:23px;color:var(--gold)}
.t4 .tag-s{left:8px;top:200px;background:var(--tag-blue)}
.t5 .kicker{top:16px;font-size:24px;color:var(--magenta)}
.t5 .big{top:37px;font-size:37px;line-height:29px;color:var(--red)}
.t5 .products{top:118px;height:70px}
.t5 .tag-s{left:61px;top:200px;background:var(--red)}
.t6{background:var(--plum)}
.t6 .photo{left:90px;background:linear-gradient(90deg,var(--plum) 0%,#a0718f 60%,#bd9aa6 100%);opacity:.8}
.t6 .kicker{top:12px;font-size:23px}
.t6 .big{top:32px;font-size:56px;line-height:42px}
.t6 .rule{left:50px;width:75px;top:129px;height:2px;background:var(--white)}
.t6 .lines{top:140px;font-size:23px;line-height:21px}
.t6 .tag-s{left:61px;top:197px;background:var(--tag-blue)}
.t7{background:var(--navy)}
.t7 .photo{left:85px;background:linear-gradient(90deg,var(--navy) 0%,#7a6676 40%,#d8d0d6 70%,#3b3038 100%)}
.t7 .lines{left:9px;top:12px;font-size:21px;line-height:19px}
.t7 .sale-box{left:9px;top:94px;width:64px;height:77px;border:1px solid var(--white)}
.t7 .sale-box span{left:4px;font-size:40px;line-height:36px}
.t7 .tag-s{left:9px;top:194px;background:var(--white);color:var(--navy)}
.t8{background:var(--royal)}
.t8 .photo{background:linear-gradient(180deg,#1b3f7c 0%,#2a66a8 50%,#16427d 100%)}
.t8 .hurry{top:80px;font-size:54px;color:var(--gold)}
.t8 .lines{top:124px;font-size:20px;line-height:18px}
.t8 .tag-plain{top:203px;font-size:9px}
.t9{background:var(--plum)}
.t9 .photo{left:95px;background:linear-gradient(90deg,var(--plum) 0%,#8c5d6a 35%,#b08a80 65%,#5a4b55 100%)}
.t9 .big{left:7px;top:12px;font-size:75px;line-height:56px}
.t9 .lines{left:8px;top:69px;font-size:24px;line-height:22px}
.t9 .tag-s{left:9px;top:199px;background:var(--tag-blue)}
</style>
</head>
<body>

<section class="tile hero">
  <div class="photo" role="img" aria-label="Smiling woman in a white cropped sweater holding a supplement bottle in a kitchen, two bottles on the counter"></div>
  <h1 class="headline">YOUR<br>SUMMER<br>BODY WON’T<br>WAIT</h1>
  <div class="sale-box"><span style="top:10px">SALE</span><span style="top:118px">NOW!</span></div>
  <p class="tag">UP TO $15 OFF</p>
</section>

<section class="tile small white t-col1 t-row1 t1">
  <p class="kicker center">FINAL COUNTDOWN TO</p>
  <p class="big center">SUMMER</p>
  <p class="red-box">SALE NOW!</p>
  <div class="products" role="img" aria-label="Row of four white supplement bottles"></div>
  <p class="tag-s">UP TO $15 OFF</p>
</section>

<section class="tile small t-col2 t-row1 t2">
  <div class="photo" role="img" aria-label="Woman in a white crop top standing behind a counter with supplement bottles"></div>
  <p class="lines">DETOX, BURN FAT,<br>AND TURN HEADS<br>THIS SUMMER</p>
  <p class="vertical">SALE NOW!</p>
  <p class="tag-box">UP TO<br>$15 OFF</p>
</section>

<section class="tile small white t-col3 t-row1 t3">
  <p class="lines center">SLIM WAIST. FLAT<br>TUMMY. MORE<br>ENERGY. LET’S GO!</p>
  <p class="red-box">SALE NOW!</p>
  <div class="products" role="img" aria-label="Row of four white supplement bottles"></div>
  <p class="tag-s">UP TO $15 OFF</p>
</section>

<section class="tile small t-col1 t-row2 t4">
  <div class="photo" role="img" aria-label="Woman in a brown top holding three supplement bottles in a living room"></div>
  <p class="lines">SUMMER’S HERE.<br>AND WE’RE<br>HAVING THE</p>
  <p class="biggest">BIGGEST<br>SALE</p>
  <p class="year">OF THE YEAR</p>
  <p class="tag-s">UP TO $15 OFF</p>
</section>

<section class="tile small white t-col2 t-row2 t5">
  <p class="kicker center">ONE SALE. ONE BODY.</p>
  <p class="big center">ONE SUMMER<br>TO SLAY</p>
  <div class="products" role="img" aria-label="Four white supplement bottles side by side"></div>
  <p class="tag-s">UP TO $15 OFF</p>
</section>

<section class="tile small t-col3 t-row2 t6">
  <div class="photo" role="img" aria-label="Faded portrait of a smiling woman on the right"></div>
  <p class="kicker center">LIMITED-TIME</p>
  <p class="big center">SUMMER<br>SALE</p>
  <div class="rule"></div>
  <p class="lines center">SNATCH YOUR<br>SUPPLEMENTS NOW!</p>
  <p class="tag-s">UP TO $15 OFF</p>
</section>

<section class="tile small t-col1 t-row3 t7">
  <div class="photo" role="img" aria-label="Woman in a white crop top holding a supplement bottle, bottles on the counter"></div>
  <p class="lines">SUMMER<br>ISN’T WAITING<br>NEITHER<br>SHOULD YOU</p>
  <div class="sale-box"><span style="top:3px">SALE</span><span style="top:39px">NOW!</span></div>
  <p class="tag-s">UP TO $15 OFF</p>
</section>

<section class="tile small t-col2 t-row3 t8">
  <div class="photo" role="img" aria-label="Blue-toned photo of a woman behind a counter lined with supplement bottles"></div>
  <p class="hurry center">HURRY!</p>
  <p class="lines center">OUR SUMMER SLIM<br>DOWN SALE IS ON<br>DON’T MISS IT!</p>
  <p class="tag-plain center">UP TO $15 OFF</p>
</section>

<section class="tile small t-col3 t-row3 t9">
  <div class="photo" role="img" aria-label="Woman in a brown top holding three supplement bottles"></div>
  <p class="big">SALE</p>
  <p class="lines">YOUR<br>SUMMER<br>BODY<br>STARTS<br>HERE</p>
  <p class="tag-s">UP TO $15 OFF</p>
</section>

</body>
</html>
```